business card for a drum shop (musical intsruments)
north ridge beats
Use same font as used in my logo
marcus hollen
4127 Garvey Oakes Ct
Lower Fenwick, Md 20691
marcus.hollen517@quellmail.net
northridgebeats.com
yes, drum image in middle with url at botton
we will upload ai file shortly. please use this for now.

```html
<!DOCTYPE html>
<html lang="en">
<head>
<meta charset="utf-8">
<title>North Ridge Beats – Business Card</title>
<link rel="stylesheet" href="https://fonts.googleapis.com/css2?family=Open+Sans:wght@300;400;600&display=swap">
<style>
  :root {
    --stage: #8f8f8f;
    --ink: #111111;
    --ink-soft: #2a2a2a;
    --paper: #ffffff;
    --paper-shade: #ececec;
    --muted: #444444;
    --on-dark: #f2f2f2;
    --font-text: "Open Sans", Arial, sans-serif;
  }
  * { box-sizing: border-box; margin: 0; padding: 0; }
  html, body { width: 1200px; height: 908px; overflow: hidden; }
  body {
    background: var(--stage);
    font-family: var(--font-text);
    display: flex;
    align-items: center;
    justify-content: center;
    gap: 50px;
  }
  .card {
    position: relative;
    width: 525px;
    height: 300px;
    border-radius: 14px;
    overflow: hidden;
  }

  /* Back side */
  .card--back {
    background: linear-gradient(160deg, var(--ink-soft) 0%, var(--ink) 70%);
  }
  .drum-artwork {
    position: absolute;
    left: 50%;
    top: 42%;
    width: 200px;
    height: 200px;
    transform: translate(-50%, -50%);
    border-radius: 50%;
    background: radial-gradient(circle at 40% 35%, #3c3c3c 0%, #262626 55%, #1a1a1a 100%);
  }
  .card--back .website {
    position: absolute;
    left: 0; right: 0;
    bottom: 26px;
    text-align: center;
    color: var(--on-dark);
    font-size: 15px;
    letter-spacing: 2px;
    font-weight: 400;
  }

  /* Front side */
  .card--front {
    background: linear-gradient(180deg, var(--paper) 0%, var(--paper) 60%, var(--paper-shade) 100%);
  }
  .brand {
    position: absolute;
    left: 34px;
    top: 32px;
    display: flex;
    align-items: center;
    gap: 12px;
  }
  .brand-dot {
    width: 38px;
    height: 38px;
    border-radius: 50%;
    background: var(--ink);
  }
  .brand-name {
    font-size: 17px;
    font-weight: 300;
    letter-spacing: 5px;
    text-transform: uppercase;
    color: var(--ink);
    line-height: 1.3;
  }
  .contact {
    position: absolute;
    left: 190px;
    top: 96px;
    color: var(--ink);
  }
  .contact .person {
    font-size: 15px;
    font-weight: 600;
    margin-bottom: 8px;
  }
  .contact .rule {
    width: 260px;
    height: 1px;
    background: var(--ink);
    margin-bottom: 8px;
  }
  .contact p {
    font-size: 10.5px;
    color: var(--muted);
    line-height: 1.55;
    display: flex;
    align-items: center;
    gap: 6px;
  }
  .contact svg { width: 11px; height: 11px; flex: none; }
  .swoosh {
    position: absolute;
    left: 0; bottom: 0;
    width: 525px;
    height: 110px;
  }
  .card--front .website {
    position: absolute;
    right: 26px;
    bottom: 16px;
    color: var(--on-dark);
    font-size: 12px;
    letter-spacing: 1.5px;
  }
</style>
</head>
<body>

  <section class="card card--back" aria-label="Business card back">
    <div class="drum-artwork" role="img" aria-label="Drum illustration with crossed sticks"></div>
    <p class="website">www.northridgebeats.com</p>
  </section>

  <section class="card card--front" aria-label="Business card front">
    <div class="brand">
      <span class="brand-dot"></span>
      <span class="brand-name">north ridge<br>beats</span>
    </div>

    <div class="contact">
      <p class="person">Marcus Hollen</p>
      <div class="rule"></div>
      <p>4127 Garvey Oakes Ct</p>
      <p>Lower Fenwick, Md 20691</p>
      <p>
        <svg viewBox="0 0 12 12"><circle cx="6" cy="6" r="5.5" fill="#111"/><path d="M4 3.2l1 1.6-.6.7c.4.9 1.1 1.6 2 2l.7-.6 1.6 1-.5 1c-2.6-.2-4.5-2.1-4.7-4.7z" fill="#fff"/></svg>
        301 555 0148
      </p>
      <p>
        <svg viewBox="0 0 12 12"><circle cx="6" cy="6" r="5.5" fill="#111"/><rect x="3" y="4" width="6" height="4" fill="none" stroke="#fff" stroke-width=".8"/><path d="M3 4l3 2.3L9 4" fill="none" stroke="#fff" stroke-width=".8"/></svg>
        marcus.hollen517@quellmail.net
      </p>
    </div>

    <svg class="swoosh" viewBox="0 0 525 110" preserveAspectRatio="none" aria-hidden="true">
      <path d="M0 70 C150 95 330 70 525 10 L525 110 L0 110 Z" fill="#111"/>
      <path d="M0 58 C170 82 340 58 525 0 L525 6 C340 66 170 92 0 66 Z" fill="#111"/>
    </svg>
    <p class="website">www.northridgebeats.com</p>
  </section>

</body>
</html>
```